International Property Consultancy

Brief Overview:

I need a dynamic and well designed website that is easy to use and understand. It has to be unique and different to generic templates that most websites seem to be these days. PLEASE NO GENERIC TEMPLATES FROM THE INTERNET.

Our business has 10 years experience working on struggling international developments that we then work in-house for to turn around and brings bout success. We stay within a project often for long periods of time until success is achieved. We are unique in our approach and completely different to the standard routes to market for many developments. The site is for developers to see what we have done in regards to previous projects, as such we want to incorporate video into this site with a strong design aesthetic. There will be videos of the past projects we have worked on, which will act as case studies.

I like very simple but punchy websites, that people can navigate and understand very easily. Also a big fan of unique and well thought out design aesthetic.

Initial Site layout thoughts:

1) Homepage:
2) About Us
3) What we've done / Work
This part has the projects we have worked on (France, Portugal, London, Morocco). Each one will have some video content and photo images, but also would be good to have a succinct way to mention what we did and the successes in a clever and punchy way.

4) Contact Us

* This is just a guideline. Would be open to input and creative direction on your own part.

*More details and websites we like can be seen in the brief doc attached.

PLEASE VIEW THE WIREFRAME WORD DOC ATTACHED.

Here there are also some more examples to help:

Here are just a few examples of websites and what I like about them:

- www.velmoro.com (clean, nice geometric design aesthetic, good animation when loading and changing pages well thought out all though also coulee be considered a bit dull and basic after the initial homepage slide)
- https://www.farbridgehub.net (Clean site, quite clinical, lacks video content and doesn't engage greatly).
- https://ruskotile.com (minimal, and like how it mixes the design aesthetic more with video and photo content)

- https://www.amberquillworks.com (like the layout of this and how it displays the projects and work section)

- https://brisk.com (Good use of video content)

- https://loomfield.studio (minimal to the point and mixes design with video and animation etc...)

Here is another couple of cool websites that may help give you some direction: https://halvenquay.com www.brisk.com

Hi there, One of the things I thought would be good on the homepage is to add the logo with a 'digital landscape' before flicking down into a slide with video content of the projects... Just an idea but have posted some pics in the brief. We would get this animated for the site. But if you have better ideas, please do run with them. Thanks,

Target Market(s)

Property developers

Number of Pages Required

4 page

Font styles to use
Other font styles liked:
• Read brief

Requirements
Must have
• Needs to be clean, dynamic and easy to follow on desktop and mobile. We will use it as a kind of portfolio website so will need to embed video of past projects we have worked on.

Read brief in docs.
Nice to have
• Clean
Should not have
• Not be another generic template website.
Not have random property stock photos. (We are not a property agency).

```html
<!DOCTYPE html>
<html lang="en">
<head>
<meta charset="utf-8">
<title>Corvantis — Mobile Screens</title>
<link href="https://fonts.googleapis.com/css2?family=Outfit:wght@300;400;500;700&display=swap" rel="stylesheet">
<style>
:root{
  --bg:#fdf5eb;
  --panel:#ffffff;
  --ink:#1f2427;
  --body:#4d5357;
  --brand:#16465a;
  --link:#7b5fd6;
  --muted:#e4e4e4;
  --icon:#3a3f42;
}
*{box-sizing:border-box;margin:0;padding:0}
html,body{width:1183px;height:1200px;overflow:hidden;background:var(--bg)}
body{font-family:"Outfit",sans-serif;color:var(--ink)}
.board{position:absolute;left:0;top:0;width:1905px;height:1932px;transform:scale(0.621);transform-origin:0 0}
.screen{position:absolute;top:74px;width:323px;background:var(--panel);overflow:hidden;box-shadow:0 50px 70px rgba(205,175,130,.22)}
.abs{position:absolute}
.logo{left:21px;top:38px;font-size:23px;font-weight:400;color:var(--brand);letter-spacing:.3px}
.menu{left:283px;top:47px;width:19px;height:11px;border-top:2px solid var(--brand);border-bottom:2px solid var(--brand)}
.h1{left:21px;font-size:28px;font-weight:400;line-height:34px;color:var(--ink)}
.lead{left:21px;width:282px;font-size:13.5px;line-height:20.7px;color:var(--body);letter-spacing:.6px;font-weight:300}
.photo{position:absolute;overflow:hidden}
.caption{position:absolute;left:21px;font-size:17px;font-weight:700;line-height:28px;color:#fff}
.play{position:absolute;width:38px;height:38px;border-radius:50%;background:rgba(30,30,30,.75);display:flex;align-items:center;justify-content:center}
.play svg{width:12px;height:12px}
.foot-mail{left:0;width:323px;text-align:center;font-size:14px;color:var(--link);letter-spacing:.6px}
.socials{left:0;width:323px;display:flex;justify-content:center;gap:27px}
.socials span{width:14px;height:14px;border-radius:50%;background:var(--icon)}
.copy{left:0;width:323px;text-align:center;font-size:12.5px;color:var(--body);letter-spacing:.8px}
.big-word{font-size:56px;font-weight:700;line-height:60px;color:var(--brand)}
</style>
</head>
<body>
<div class="board">

  <!-- Home -->
  <section class="screen" style="left:69px;height:1231px">
    <div class="abs logo">Corvantis.</div><div class="abs menu"></div>
    <h1 class="abs h1" style="top:115px">We are Corvantis</h1>
    <p class="abs lead" style="top:157px">We fulfill international property developments</p>
    <div class="photo" role="img" aria-label="Curved glass facade towers against blue sky" style="left:21px;top:234px;width:282px;height:292px;background:linear-gradient(160deg,#1d4f86,#3b7fb0 50%,#12305a)">
      <div class="abs" style="left:0;top:133px;width:282px;text-align:center;color:#fff;font-size:19px">Corvantis.</div>
    </div>
    <h2 class="abs h1" style="top:592px">Case Studies</h2>
    <p class="abs lead" style="top:634px">We deliver a unique and truly bespoke approach to delivering international developments to market, with over 10 years success around the world.</p>
    <div class="photo" role="img" aria-label="Woven metal building facade under blue sky" style="left:49px;top:766px;width:193px;height:227px;background:linear-gradient(180deg,#217ba0 0%,#2f88a8 40%,#9fb6c0 75%,#c9d2d6)"></div>
    <div class="photo" role="img" aria-label="Glass tower detail" style="left:299px;top:766px;width:40px;height:227px;background:linear-gradient(180deg,#7fa6c0,#b8cad6)"></div>
    <div class="abs big-word" style="left:21px;top:910px">France</div>
    <div class="abs big-word" style="left:21px;top:910px;color:#fff;clip-path:inset(0 0 0 28px)">France</div>
    <div class="abs big-word" style="left:271px;top:910px">Mo</div>
    <div class="abs foot-mail" style="top:1094px">info@corvantis.com</div>
    <div class="abs socials" style="top:1135px"><span></span><span></span><span></span><span></span></div>
    <div class="abs copy" style="top:1183px">Copyright © 2020 Corvantis</div>
  </section>

  <!-- Case study: France -->
  <section class="screen" style="left:430px;height:1719px">
    <div class="abs logo">Corvantis.</div><div class="abs menu"></div>
    <h1 class="abs h1" style="top:115px">France</h1>
    <p class="abs lead" style="top:157px">Augue eget nisi, turpis vel nibh urna, ut quam odio libero.</p>
    <div class="photo" role="img" aria-label="Woven metal facade video still" style="left:21px;top:234px;width:282px;height:292px;background:linear-gradient(180deg,#217ba0 0%,#2d86a8 40%,#9cb3bd 75%,#cdd5d8)">
      <div class="abs" style="left:0;top:124px;width:282px;text-align:center;color:#fff;font-size:30px;font-weight:500">France</div>
      <div class="play" style="left:122px;top:127px"><svg viewBox="0 0 12 12"><path d="M2 1l9 5-9 5z" fill="#fff"/></svg></div>
    </div>
    <h2 class="abs h1" style="top:592px">The challenge</h2>
    <p class="abs lead" style="top:641px">Augue eget nisi, turpis vel nibh urna, ut quam odio libero, aliquam, morbi proin feugiat nisl mattis enim venenatis nunc, malesuada urna, viverra massa lacus pellentesque lacus, tortor eleifend egestas vitae dignissim odio arcu nunc scelerisque nisl nunc gravida id egestas eros ullamcorper turpis orci id mattis ipsum sit adipiscing</p>
    <div class="photo" role="img" aria-label="White modern apartment building" style="left:21px;top:856px;width:282px;height:197px;background:linear-gradient(160deg,#dfe6ea,#c5d3dc 60%,#9fb0bb)">
      <div class="caption" style="top:122px">Ac elit nisl, sem urna<br>gravida</div>
    </div>
    <div class="photo" role="img" aria-label="Dark glass building against turquoise sky" style="left:21px;top:1074px;width:282px;height:196px;background:linear-gradient(100deg,#7fe0c4,#3fcfbf 45%,#1d4a52 70%,#0e2c36)">
      <div class="caption" style="top:120px">Ac elit nisl, sem urna gravida<br>eget in nibh eleifend</div>
    </div>
    <div class="photo" role="img" aria-label="Layered balconies of a modern building under cloudy sky" style="left:21px;top:1305px;width:282px;height:420px;background:linear-gradient(160deg,#8cc3dc,#d9d2c4 50%,#8c8a86 85%,#5e5d5b)">
      <div class="caption" style="top:336px">Ac elit nisl, sem urna gravida<br>eget in nibh eleifend</div>
    </div>
  </section>

  <!-- Case study: detail -->
  <section class="screen" style="left:791px;height:1719px">
    <div class="photo" role="img" aria-label="Building detail" style="left:21px;top:0;width:282px;height:57px;background:linear-gradient(90deg,#3e3e3c,#6e6b66 50%,#a29f99)">
      <div class="caption" style="top:8px">eget in nibh eleifend</div>
    </div>
    <p class="abs" style="left:21px;top:127px;width:290px;font-size:18px;line-height:31px;letter-spacing:.6px;color:var(--body)">Augue eget nisi, turpis vel nibh urna, ut quam odio libero, aliquam, morbi proin feugiat nisl mattis enim venenatis nunc, malesuada urna, viverra massa lacus pellentesque lacus, tortor eleifend egestas vitae dignissim odio arcu nunc scelerisque nisl nunc gravida id egestas eros ullamcorper turpis orci id mattis ipsum sit adipiscing</p>
    <div class="photo" role="img" aria-label="Grey clad building corner against sky" style="left:21px;top:538px;width:212px;height:156px;background:linear-gradient(120deg,#2f3740,#4f5a66 50%,#a7c4dc)"></div>
    <div class="photo" role="img" aria-label="Copper and dark panel facade" style="left:252px;top:538px;width:80px;height:156px;background:linear-gradient(90deg,#b8683e,#8a4a2c 50%,#0f2a30)"></div>
    <div class="abs" style="left:21px;top:721px;width:282px;height:1px;background:var(--muted)"></div>
    <div class="abs" style="left:21px;top:720px;width:108px;height:2px;background:var(--ink)"></div>
    <h2 class="abs h1" style="top:788px">Solution</h2>
    <p class="abs lead" style="top:830px">Augue eget nisi, turpis vel nibh urna, ut quam odio libero, aliquam, morbi proin feugiat nisl mattis enim venenatis nunc, malesuada urna, viverra massa lacus pellentesque lacus, tortor eleifend egestas vitae dignissim odio arcu nunc scelerisque nisl nunc gravida id egestas eros ullamcorper turpis orci id mattis ipsum sit adipiscing</p>
    <div class="photo" role="img" aria-label="White amphitheatre steps video still" style="left:21px;top:1053px;width:282px;height:290px;background:linear-gradient(180deg,#b7d5df 0%,#dfe6e6 35%,#efe6d8 50%,#d8dbdc 75%,#c4c8ca)">
      <div class="play" style="left:122px;top:126px"><svg viewBox="0 0 12 12"><path d="M2 1l9 5-9 5z" fill="#fff"/></svg></div>
    </div>
    <p class="abs lead" style="top:1378px">Proin neque lectus eu, porttitor sollicitudin sed ipsum et integer quam commodo quis sit volutpat lorem molestie sed aliquet sagittis fermentum amet, lobortis odio tempus id eleifend condimentum bibendum donec viverra dictum scelerisque in ultricies non, rhoncus volutpat quam risus blandit a egestas nunc sed nam nisl lectus vulputate eget bibendum justo enim malesuada suscipit egestas lacus blandit massa habitant mauris phasellus sociis vestibulum interdum tempor cursus semper malesuada neque amet, rhoncus, bibendum eu fringilla eu lacus libero nulla tellus pretium massa tortor neque purus</p>
  </section>

  <!-- Contact -->
  <section class="screen" style="left:1152px;height:804px">
    <div class="abs logo">Corvantis.</div><div class="abs menu"></div>
    <h1 class="abs" style="left:21px;top:116px;font-size:35px;font-weight:400;line-height:48.5px">Hello<br>Bonjour<br>Olá<br>marhabaan</h1>
    <h2 class="abs" style="left:21px;top:380px;font-size:20px;font-weight:400">Contact us</h2>
    <p class="abs lead" style="top:434px">info@corvantis.com</p>
    <p class="abs lead" style="top:468px">+555 2041 87 33</p>
    <p class="abs lead" style="top:503px">1842 N. Alder Rd.<br>Easton, Pennsylvania<br>18040</p>
    <div class="abs foot-mail" style="top:666px">info@corvantis.com</div>
    <div class="abs socials" style="top:708px"><span></span><span></span><span></span><span></span></div>
    <div class="abs copy" style="top:756px">Copyright © 2020 Corvantis</div>
  </section>

  <!-- About -->
  <section class="screen" style="left:1512px;height:1329px">
    <div class="abs logo">Corvantis.</div><div class="abs menu"></div>
    <h1 class="abs h1" style="top:115px">About us</h1>
    <p class="abs lead" style="top:157px">Augue eget nisi, turpis vel nibh urna, ut quam odio libero, aliquam, morbi proin feugiat nisl mattis enim venenatis nunc, malesuada urna, viverra massa lacus pellentesque lacus, tortor eleifend egestas vitae dignissim odio arcu nunc scelerisque nisl nunc gravida id egestas eros ullamcorper turpis orci id mattis ipsum sit adipiscing</p>
    <p class="abs lead" style="top:385px">Massa vitae aliquam condimentum diam aliquam suspendisse diam in in egestas congue eget fringilla neque suspendisse diam, ultrices interdum tristique.</p>
    <p class="abs" style="left:21px;top:522px;width:282px;font-size:20px;line-height:28px;color:var(--brand)">We'd love to learn more about your project.</p>
    <div class="abs" style="left:21px;top:614px;width:282px;height:48px;background:var(--brand);color:#fff;display:flex;align-items:center;justify-content:center;gap:14px;font-size:16px">Let's Talk
      <svg width="26" height="12" viewBox="0 0 26 12"><path d="M0 6h24M19 1l5 5-5 5" stroke="#fff" stroke-width="1.5" fill="none"/></svg></div>
    <h2 class="abs h1" style="top:729px">Meet our team</h2>
    <div class="photo" role="img" aria-label="Black and white portrait of a team member" style="left:21px;top:799px;width:211px;height:223px;background:linear-gradient(180deg,#bdbdbd,#8a8a8a 60%,#2a2a2a)"></div>
    <div class="photo" role="img" aria-label="Black and white portrait of a team member" style="left:253px;top:799px;width:80px;height:223px;background:linear-gradient(180deg,#6e6e6e,#3a3a3a)"></div>
    <div class="abs" style="left:21px;top:1042px;font-size:21px">Member Name</div>
    <div class="abs" style="left:21px;top:1077px;font-size:10.5px;color:var(--body)">Ceo/Founder, Designation</div>
    <div class="abs" style="left:253px;top:1042px;font-size:21px;white-space:nowrap">Member Name</div>
    <div class="abs" style="left:253px;top:1077px;font-size:10.5px;color:var(--body);white-space:nowrap">Ceo/Founder, Designation</div>
    <div class="abs foot-mail" style="top:1191px">info@corvantis.com</div>
    <div class="abs socials" style="top:1233px"><span></span><span></span><span></span><span></span></div>
    <div class="abs copy" style="top:1281px">Copyright © 2020 Corvantis</div>
  </section>

</div>
</body>
</html>
```